VALMIKE GROUP

This is a company that provides executive protection. Our motto is "New Era in Protection"... I don't want this to look like other security websites. I want it to be clean and sharp and represent a new era. We are based in the bay area so maybe a picture of San Francisco in the background?
I want it to be able to funnel down a couple different categories.
1. About Us
2. Services (Executive Protection, Covert Protection, Residential Protection & Intelligence)
3. Iron Finch (Training & Consulting)
4. Contact Us
I want it to be very clean and modern. I don't want there to be any pictures of bodyguards with ear pieces like every other website.
Target Market(s)
Ultra High Net Worth Individuals
Coding
Coded - Design and coding required
Number of Pages Required
1 page
Requirements
Must have
- Colors of my Symbol
Nice to have
- City in the background, San Francisco, New York or the Pinehallow Club in Montana.
Should not have
- Should not look like an KVM website or have photos of bodyguards. I want this to be a clean and simple website with my logo

```html
<!DOCTYPE html>
<html lang="en">
<head>
<meta charset="utf-8">
<title>VALMIKE GROUP — New Era in Protection</title>
<link href="https://fonts.googleapis.com/css2?family=Poppins:wght@400;500;600;700&display=swap" rel="stylesheet">
<style>
:root{
  --red:#e31e24;
  --red-dark:#8e1519;
  --ink:#1f2230;
  --text:#333;
  --muted:#555;
  --topbar:#2a2a2a;
  --charcoal:#231f20;
  --footer:#2b2b2b;
  --light:#ebebeb;
  --white:#fff;
  --btn:linear-gradient(90deg,#e31e24,#8e1519);
}
*{margin:0;padding:0;box-sizing:border-box}
html,body{width:1200px;height:4289px;overflow:hidden}
body{font-family:"Poppins",sans-serif;color:var(--text);background:var(--white)}
.page{position:relative;width:1200px;height:4289px;overflow:hidden}
.abs{position:absolute}
.btn{position:absolute;display:flex;align-items:center;justify-content:center;background:var(--btn);color:var(--white);border-radius:30px;font-weight:600;text-decoration:none;box-shadow:0 4px 10px rgba(0,0,0,.2)}

/* top bar */
.topbar{top:0;left:0;width:1200px;height:20px;background:var(--topbar);color:var(--white);font-size:10px}
.topbar span{position:absolute;top:3px}
.topbar svg{vertical-align:-2px;margin-right:5px}

/* header */
.header{top:20px;left:0;width:1200px;height:96px;background:var(--white)}
.brand{position:absolute;left:188px;top:30px;display:flex;align-items:center;gap:8px;font-weight:700;font-size:17px;color:var(--ink);letter-spacing:.5px}
.brand i{display:block;width:14px;height:14px;background:var(--red)}
.nav a{position:absolute;top:30px;font-size:14px;color:var(--text);text-decoration:none;height:42px;line-height:42px}
.nav a.active{border:2px solid var(--red);padding:0 14px 0 38px;line-height:38px;color:var(--red)}
.nav a.active i{position:absolute;left:12px;top:12px;width:14px;height:14px;border:2px solid var(--red)}

/* hero */
.hero-photo{top:116px;left:0;width:1200px;height:620px}
.hero-arrow{top:275px;width:67px;height:46px}
.hero h1{position:absolute;top:266px;left:0;width:1200px;text-align:center;color:var(--white);font-size:44px;font-weight:700;line-height:49px}
.hero p{position:absolute;top:384px;left:0;width:1200px;text-align:center;color:var(--white);font-size:18px;font-weight:500;line-height:22px}

/* welcome */
.welcome-rule{top:792px;left:183px;width:70px;height:4px;background:var(--ink)}
.welcome-title{top:780px;left:260px;font-size:28px;font-weight:700;color:var(--ink)}
.welcome-lead{top:826px;left:261px;width:730px;font-size:19px;font-weight:600;line-height:31px;color:var(--ink)}
.dots{top:932px;left:185px;width:243px;height:220px;background:#efefef}
.welcome-visual{top:970px;left:261px;width:291px;height:311px;background:linear-gradient(150deg,#5a0f14,#9b2a32 55%,#3a0a0d)}
.welcome-copy{top:970px;left:609px;width:390px;font-size:13px;line-height:23px;color:var(--text)}
.welcome-copy strong{display:block;font-weight:600;color:var(--ink);margin-bottom:23px}

/* services */
.section-title{font-size:28px;font-weight:700;color:var(--ink);text-align:center;width:1200px;left:0}
.section-rule{height:4px;background:var(--ink)}
.card{position:absolute;top:1478px;width:263px;height:372px;background:var(--white);box-shadow:0 0 14px rgba(0,0,0,.12);text-align:center}
.card .bar{position:absolute;left:0;bottom:0;width:100%;height:20px;background:var(--btn)}
.card svg{position:absolute;left:50%;transform:translateX(-50%);top:28px}
.card h3{position:absolute;top:106px;left:0;width:100%;font-size:18px;font-weight:500;color:var(--ink);line-height:20px}
.card .tick{position:absolute;left:50%;transform:translateX(-50%);width:60px;height:3px;background:var(--red)}
.card p{position:absolute;left:28px;width:207px;font-size:11.5px;line-height:20px;color:var(--muted)}
.card .btn{left:64px;top:268px;width:136px;height:36px;font-size:12px}

/* training */
.training{top:2025px;left:0;width:1200px;height:687px;background:var(--charcoal)}
.training h2{position:absolute;top:86px;left:183px;font-size:43px;font-weight:700;color:var(--red);letter-spacing:-.5px}
.training .lead{position:absolute;top:158px;left:183px;width:560px;font-size:19px;font-weight:600;line-height:28px;color:var(--white)}
.tile{position:absolute;top:285px;width:192px;height:258px;background:var(--white);text-align:center}
.tile.hot{background:var(--btn)}
.tile svg{position:absolute;top:36px;left:73px}
.tile h4{position:absolute;top:92px;width:100%;font-size:15px;font-weight:400;color:var(--red)}
.tile p{position:absolute;top:120px;left:22px;width:148px;font-size:11px;line-height:17px;color:var(--text)}
.tile a{position:absolute;top:198px;left:0;width:100%;font-size:10.5px;letter-spacing:1.3px;color:var(--ink);text-decoration:none;font-weight:500}
.tile a::after{content:"";display:block;width:70px;height:2px;background:var(--red);margin:4px auto 0}
.tile.hot h4,.tile.hot p,.tile.hot a{color:var(--white)}
.tile.hot a::after{background:var(--white)}

/* contact */
.map{top:2712px;left:0;width:527px;height:678px;background:linear-gradient(160deg,#e7e4d8,#d9e4c8 45%,#b9cdef 75%,#e3e6ea)}
.contact-title{top:2808px;left:589px;font-size:27px;font-weight:700;color:var(--ink)}
.contact-sub{top:2846px;left:589px;font-size:18px;letter-spacing:1.6px;color:var(--muted)}
.label{position:absolute;left:589px;font-size:14px;font-weight:500;color:var(--ink)}
.label b{color:var(--red);font-weight:500}
.field{position:absolute;left:591px;width:426px;border:1.5px solid #a9a9a9;box-shadow:0 0 4px rgba(0,0,0,.15);font-size:10px;color:#777;padding:11px 10px}

/* advice */
.advice{top:3390px;left:0;width:1200px;height:438px;background:var(--light)}
.advice p{position:absolute;top:155px;left:0;width:1200px;text-align:center;font-size:30px;font-weight:500;line-height:40px;color:#3d3d3d}

/* footer */
.footer{top:3828px;left:0;width:1200px;height:461px;background:var(--footer);color:var(--white)}
.fcol{position:absolute;top:100px}
.fcol h5{font-size:15px;font-weight:500;color:var(--red);margin-bottom:12px}
.fcol li{list-style:none;font-size:13.5px;line-height:31.5px}
.fcol li svg{vertical-align:-2px;margin-right:10px}
.fcol .follow{font-size:11px;margin-top:4px}
.socials{display:flex;gap:8px;margin-top:6px}
.socials i{display:block;width:12px;height:12px;background:var(--red)}
.news-input{position:absolute;top:131px;left:825px;width:190px;height:33px;background:var(--white);color:#888;font-size:10px;padding:10px}
.news-btn{position:absolute;top:176px;left:825px;width:190px;height:33px;background:var(--btn);color:var(--white);font-size:11px;font-weight:600;text-align:center;line-height:33px}
.fdivider{position:absolute;top:366px;left:0;width:1200px;height:1px;background:#444}
.fbrand{position:absolute;top:386px;left:183px;font-size:16px;font-weight:700;letter-spacing:.5px}
.copy{position:absolute;top:391px;left:872px;font-size:11px;font-weight:600}
.copy span{color:var(--red)}
</style>
</head>
<body>
<div class="page">

  <div class="abs topbar">
    <span style="left:186px">Welcome to our website</span>
    <span style="left:700px"><svg width="10" height="10" viewBox="0 0 24 24"><path fill="#fff" d="M6.6 10.8a15 15 0 006.6 6.6l2.2-2.2c.3-.3.7-.4 1-.2 1.1.4 2.3.6 3.6.6.6 0 1 .4 1 1V20c0 .6-.4 1-1 1A17 17 0 013 4c0-.6.4-1 1-1h3.5c.6 0 1 .4 1 1 0 1.3.2 2.5.6 3.6.1.3 0 .7-.2 1z"/></svg><b>Ph :</b> 1800 555 0147</span>
    <span style="left:854px"><svg width="12" height="10" viewBox="0 0 24 18"><rect x="1" y="1" width="22" height="16" fill="none" stroke="#fff" stroke-width="2"/><path d="M1 1l11 9 11-9" fill="none" stroke="#fff" stroke-width="2"/></svg><b>Email :</b> hello@valmike-mail.com</span>
  </div>

  <header class="abs header">
    <div class="brand"><i></i>VALMIKE GROUP</div>
    <nav class="nav">
      <a class="active" href="#" style="left:486px"><i></i>Home</a>
      <a href="#" style="left:614px">About Us</a>
      <a href="#" style="left:719px">Services</a>
      <a href="#" style="left:819px">Iron Finch</a>
      <a href="#" style="left:923px">Contact Us</a>
    </nav>
  </header>

  <section class="hero">
    <svg class="abs hero-photo" viewBox="0 0 1200 620" role="img" aria-label="Night skyline of a city with lit skyscrapers">
      <defs>
        <linearGradient id="sky" x1="0" y1="0" x2="0" y2="1">
          <stop offset="0" stop-color="#2b2a33"/>
          <stop offset=".35" stop-color="#6b4a2e"/>
          <stop offset=".6" stop-color="#3a2c22"/>
          <stop offset="1" stop-color="#1c1a1d"/>
        </linearGradient>
      </defs>
      <polygon points="0,0 1200,0 1200,330 600,620 0,330" fill="url(#sky)"/>
    </svg>
    <svg class="abs hero-arrow" style="left:8px" viewBox="0 0 67 46"><path d="M18 2h47v42H18L2 23z" fill="none" stroke="#fff" stroke-width="3"/><path d="M38 16l-7 7 7 7M46 16l-7 7 7 7" fill="none" stroke="#fff" stroke-width="3"/></svg>
    <svg class="abs hero-arrow" style="left:1115px" viewBox="0 0 67 46"><path d="M49 2H2v42h47l16-21z" fill="none" stroke="#fff" stroke-width="3"/><path d="M21 16l7 7-7 7M29 16l7 7-7 7" fill="none" stroke="#fff" stroke-width="3"/></svg>
    <h1>Type specimen book. It has<br>survived not only five</h1>
    <p>Unknown printer took a galley of type and scrambled it<br>to make a type</p>
    <a class="btn" href="#" style="left:486px;top:479px;width:233px;height:64px;font-size:20px;font-weight:500">Get In touch</a>
  </section>

  <section class="welcome">
    <div class="abs welcome-rule"></div>
    <h2 class="abs welcome-title">WELCOME</h2>
    <p class="abs welcome-lead">Unknown printer took a galley of type and scrambled it to make a type specimen book. It has survived not only five centuries, but also the leap into electronic typesetting, remaining essentially unchanged.</p>
    <div class="abs dots" role="img" aria-label="Light dotted background pattern"></div>
    <div class="abs welcome-visual" role="img" aria-label="Brand symbol filled with a night bridge photograph in deep red tones"></div>
    <div class="abs welcome-copy">
      <strong>Unknown printer took a galley of type and scrambled it to make a type specimen book. Iat has survived not only five centuries, but also the leap into</strong>
      electronic typesetting, remaining essentially unchanged. Unknown printer took a galley of type and scrambled it to make a type specimen book. Iat has survived not only five centuries, but also the leap into electronic typesetting, remaining essentially unchanged.
    </div>
    <a class="btn" href="#" style="left:611px;top:1210px;width:136px;height:36px;font-size:12px">Read More</a>
  </section>

  <section class="services">
    <h2 class="abs section-title" style="top:1362px">OUR SERVICES</h2>
    <div class="abs section-rule" style="top:1402px;left:566px;width:70px"></div>

    <article class="card" style="left:183px">
      <svg width="50" height="60" viewBox="0 0 50 60"><circle cx="25" cy="12" r="9" fill="none" stroke="#e31e24" stroke-width="2.5"/><path d="M6 58V36c0-8 8-14 19-14s19 6 19 14v22z" fill="none" stroke="#e31e24" stroke-width="2.5"/><path d="M25 24v20" stroke="#e31e24" stroke-width="2.5"/></svg>
      <h3>Executive Protection</h3>
      <div class="tick" style="top:134px"></div>
      <p style="top:152px">Unknown printer took a galley of type and scrambled it to make a type specimen book. It has survived not only five centuries,</p>
      <a class="btn" href="#">Read More</a>
      <div class="bar"></div>
    </article>

    <article class="card" style="left:469px">
      <svg width="52" height="62" viewBox="0 0 52 62"><path d="M26 2L4 10v18c0 16 10 27 22 32 12-5 22-16 22-32V10z" fill="#e31e24"/><path d="M26 2v58c12-5 22-16 22-32V10z" fill="#a8161b"/></svg>
      <h3>Covert Protection</h3>
      <div class="tick" style="top:134px"></div>
      <p style="top:152px">Unknown printer took a galley of type and scrambled it to make a type specimen book. It has survived not only five centuries,</p>
      <a class="btn" href="#">Read More</a>
      <div class="bar"></div>
    </article>

    <article class="card" style="left:754px">
      <svg width="64" height="62" viewBox="0 0 64 62" fill="none" stroke="#e31e24" stroke-width="2"><circle cx="32" cy="6" r="5"/><circle cx="6" cy="31" r="5"/><circle cx="58" cy="31" r="5"/><circle cx="32" cy="56" r="5"/><circle cx="19" cy="18" r="4"/><circle cx="45" cy="18" r="4"/><circle cx="19" cy="44" r="4"/><circle cx="45" cy="44" r="4"/><circle cx="32" cy="31" r="5"/><path d="M28 9l-6 6M36 9l6 6M9 27l7-6M55 27l-7-6M9 35l7 6M55 35l-7 6M28 53l-6-6M36 53l6-6"/></svg>
      <h3>Residential Protection<br>&amp; Intelligence</h3>
      <div class="tick" style="top:154px"></div>
      <p style="top:170px">Unknown printer took a galley of type and scrambled it to make a type specimen book. It has survived not only five centuries,</p>
      <a class="btn" href="#">Read More</a>
      <div class="bar"></div>
    </article>
  </section>

  <section class="abs training">
    <h2>TRAINING &amp; CONSULTING</h2>
    <p class="lead">Unknown printer took a galley of type and scrambled it to make a type specimen book. Iat has survived not only five centuries, but also the leap into</p>

    <article class="tile" style="left:183px">
      <svg width="46" height="46" viewBox="0 0 46 46" fill="none" stroke="#e31e24" stroke-width="2"><circle cx="23" cy="23" r="21"/><path d="M14 31h18M16 30v-5M21 30v-8M26 30v-11M31 30v-14M14 22l8-6 5 3 7-6"/></svg>
      <h4>Headlline 1</h4>
      <p>Unknown printer took a galley of type and scrambled it to make a type specimen</p>
      <a href="#">READ MORE</a>
    </article>
    <article class="tile" style="left:398px">
      <svg width="46" height="46" viewBox="0 0 46 46" fill="none" stroke="#e31e24" stroke-width="2"><circle cx="23" cy="23" r="21"/><rect x="14" y="16" width="18" height="16"/><path d="M18 12h10v4M18 22h10M18 27h6"/></svg>
      <h4>Headlline 2</h4>
      <p>Unknown printer took a galley of type and scrambled it to make a type specimen</p>
      <a href="#">READ MORE</a>
    </article>
    <article class="tile hot" style="left:612px">
      <svg width="46" height="46" viewBox="0 0 46 46" fill="none" stroke="#fff" stroke-width="2"><circle cx="23" cy="23" r="21"/><circle cx="23" cy="23" r="4"/><circle cx="23" cy="12" r="3"/><circle cx="23" cy="34" r="3"/><circle cx="13" cy="18" r="3"/><circle cx="33" cy="18" r="3"/><circle cx="13" cy="28" r="3"/><circle cx="33" cy="28" r="3"/></svg>
      <h4>Headlline 3</h4>
      <p>Unknown printer took a galley of type and scrambled it to make a type specimen</p>
      <a href="#">READ MORE</a>
    </article>
    <article class="tile" style="left:825px">
      <svg width="46" height="46" viewBox="0 0 46 46" fill="none" stroke="#e31e24" stroke-width="2"><circle cx="23" cy="23" r="21"/><path d="M23 12a8 8 0 00-5 14v4h10v-4a8 8 0 00-5-14zM19 34h8"/><path d="M23 6v2M11 11l2 2M35 11l-2 2M7 22h2M37 22h2"/></svg>
      <h4>Headlline 4</h4>
      <p>Unknown printer took a galley of type and scrambled it to make a type specimen</p>
      <a href="#">READ MORE</a>
    </article>
  </section>

  <section class="contact">
    <div class="abs map" role="img" aria-label="Street map of the harbor area and surrounding towns"></div>
    <h2 class="abs contact-title">LET'S WORK TOGETHER</h2>
    <p class="abs contact-sub">We bring the breathe of our experience.</p>
    <label class="label" style="top:2890px">Your Name<b>*</b></label>
    <div class="field" style="top:2916px;height:42px">Enter Your Name :</div>
    <label class="label" style="top:2965px">Your Email<b>*</b></label>
    <div class="field" style="top:2990px;height:41px">Enter Your Email :</div>
    <label class="label" style="top:3040px">Subject<b>*</b></label>
    <div class="field" style="top:3067px;height:40px">Enter your phone :</div>
    <label class="label" style="top:3115px">Your Message<b>*</b></label>
    <div class="field" style="top:3142px;height:108px">Enter Your Message :</div>
    <a class="btn" href="#" style="left:586px;top:3270px;width:136px;height:37px;font-size:12px">Read More</a>
  </section>

  <section class="abs advice">
    <p>Your goals are individual. We believe financial<br>advice should be too.</p>
    <a class="btn" href="#" style="left:508px;top:256px;width:136px;height:38px;font-size:12px">Read More</a>
  </section>

  <footer class="abs footer">
    <div class="fcol" style="left:183px">
      <h5>Sitemap</h5>
      <ul><li>Home</li><li>About Us</li><li>Services</li><li>Iron Finch</li><li>Contact Us</li></ul>
    </div>
    <div class="fcol" style="left:374px">
      <h5>Services</h5>
      <ul><li>Home</li><li>About Us</li><li>Services</li><li>Iron Finch</li><li>Contact Us</li></ul>
    </div>
    <div class="fcol" style="left:543px">
      <h5>Connect</h5>
      <ul>
        <li><svg width="12" height="12" viewBox="0 0 24 24"><path fill="#e31e24" d="M6.6 10.8a15 15 0 006.6 6.6l2.2-2.2c.3-.3.7-.4 1-.2 1.1.4 2.3.6 3.6.6.6 0 1 .4 1 1V20c0 .6-.4 1-1 1A17 17 0 013 4c0-.6.4-1 1-1h3.5c.6 0 1 .4 1 1 0 1.3.2 2.5.6 3.6.1.3 0 .7-.2 1z"/></svg>1-800-555-0192</li>
        <li><svg width="12" height="14" viewBox="0 0 20 26"><path d="M10 1a8 8 0 00-8 8c0 6 8 15 8 15s8-9 8-15a8 8 0 00-8-8z" fill="none" stroke="#e31e24" stroke-width="2"/><circle cx="10" cy="9" r="3" fill="#e31e24"/></svg>48 Harbor Lane, San Francisco</li>
        <li><svg width="12" height="10" viewBox="0 0 24 18"><rect x="1" y="1" width="22" height="16" fill="none" stroke="#e31e24" stroke-width="2"/><path d="M1 1l11 9 11-9" fill="none" stroke="#e31e24" stroke-width="2"/></svg>info@valmike-group.com</li>
      </ul>
      <p class="follow">Follow un on</p>
      <div class="socials"><i></i><i></i><i></i><i></i></div>
    </div>
    <div class="fcol" style="left:825px">
      <h5>Newsletter Subscribe</h5>
    </div>
    <div class="news-input">Enter your email id :</div>
    <div class="news-btn">Subscribe Now</div>
    <div class="fdivider"></div>
    <div class="fbrand">VALMIKE GROUP</div>
    <p class="copy">Copyright © 2021 <span>VALMIKE</span></p>
  </footer>

</div>
</body>
</html>
```